Logo for a small law firm
phrase "Trial Lawyers" should appear
Professional
Colby, Fenwick & Lusk
R. Tomasz Colby
3817 SW 58th Avenue Suite 314 Miami, Florida 33155
tomasz@colbylegal.net
The name of the firm should appear at the top and the phrase "Trial Lawyers" below it
rtomaszcolby rtomaszcolby
Yes, of course. The name is Colby, Fenwick & Lusk. I am looking for a professional business logo/tradename for use on all stationery.
VelunoStudioWorks VelunoStudioWorks
Hi Sir/Madam, Can you please tell me the firm name which you want to put in the logo and which kind of logo you want? Thnx.

```html
<!DOCTYPE html>
<html lang="en">
<head>
<meta charset="utf-8">
<title>Colby, Fenwick &amp; Lusk — Business Card</title>
<link rel="stylesheet" href="https://fonts.googleapis.com/css2?family=Cinzel:wght@500&family=Jost:wght@400;500&display=swap">
<style>
  :root {
    --navy: #14244f;
    --navy-deep: #0e1a3c;
    --gold: #e59a2a;
    --paper: #ffffff;
    --paper-shade: #e6e8ec;
    --ink: #3a3f4b;
    --stage: #d9dadc;
  }
  * { box-sizing: border-box; margin: 0; padding: 0; }
  html, body { width: 1200px; height: 904px; overflow: hidden; }
  body {
    background: var(--stage);
    font-family: "Jost", sans-serif;
    position: relative;
  }
  .card {
    position: absolute;
    left: 240px;
    width: 720px;
    height: 411px;
    border-radius: 4px;
    box-shadow: 0 6px 18px rgba(0,0,0,.18);
    overflow: hidden;
  }
  .card--front { top: 28px; background: var(--navy); }
  .card--back {
    top: 465px;
    background: radial-gradient(ellipse at 40% 35%, var(--paper) 45%, var(--paper-shade) 100%);
  }

  .firm-name {
    font-family: "Cinzel", serif;
    font-weight: 500;
    color: var(--gold);
    letter-spacing: .5px;
    white-space: nowrap;
  }
  .tagline { font-family: "Jost", sans-serif; font-weight: 400; white-space: nowrap; }

  /* Front */
  .front-brand {
    position: absolute;
    left: 50%; top: 50%;
    transform: translate(-50%, -50%);
    text-align: center;
  }
  .front-brand .rule { height: 1px; background: var(--paper); width: 100%; margin-bottom: 8px; opacity: .85; }
  .front-brand .firm-name { font-size: 30px; }
  .front-brand .tagline { color: var(--paper); font-size: 20px; margin-top: 2px; }

  /* Back */
  .back-brand { position: absolute; left: 64px; top: 58px; }
  .back-brand .rule { height: 1px; background: var(--navy); width: 100%; margin-bottom: 6px; }
  .back-brand .firm-name { font-size: 24px; }
  .back-brand .tagline { color: var(--navy); font-size: 17px; margin-top: 1px; }

  .holder-name {
    position: absolute;
    right: 64px; top: 96px;
    color: var(--navy);
    font-size: 22px;
    font-weight: 500;
  }
  .divider {
    position: absolute;
    left: 56px; right: 56px; top: 190px;
    border-top: 2px dotted #9aa0ab;
  }
  .address {
    position: absolute;
    left: 64px; top: 222px;
    color: var(--ink);
    font-size: 14px;
    line-height: 1.45;
    font-style: normal;
  }
  .contacts {
    position: absolute;
    left: 64px; top: 312px;
    list-style: none;
    color: var(--ink);
    font-size: 14px;
  }
  .contacts li { display: flex; align-items: center; gap: 10px; height: 24px; }
  .contacts svg { width: 14px; height: 14px; fill: var(--gold); }

  .corner-band { position: absolute; right: 0; bottom: 0; width: 720px; height: 411px; }
  .website {
    position: absolute;
    right: 30px; top: 210px;
    color: var(--paper);
    font-size: 14px;
    letter-spacing: 1.5px;
  }
</style>
</head>
<body>

<section class="card card--front" aria-label="Card front">
  <div class="front-brand">
    <div class="rule"></div>
    <div class="firm-name">Colby, Fenwick &amp; Lusk</div>
    <div class="tagline">Trial Lawyers</div>
  </div>
</section>

<section class="card card--back" aria-label="Card back">
  <svg class="corner-band" viewBox="0 0 720 411" aria-hidden="true">
    <polygon points="470,196 720,196 720,240 454,240" fill="var(--navy)"/>
    <polygon points="452,246 720,246 720,262 446,262" fill="var(--gold)"/>
    <polygon points="444,268 720,268 720,411 0,411 0,396 420,396" fill="var(--navy)"/>
  </svg>

  <div class="back-brand">
    <div class="rule"></div>
    <div class="firm-name">Colby, Fenwick &amp; Lusk</div>
    <div class="tagline">Trial Lawyers</div>
  </div>

  <div class="holder-name">R. Tomasz Colby</div>
  <div class="divider"></div>
  <div class="website">colbylegal.net</div>

  <address class="address">
    3817 SW 58th Avenue<br>
    Suite 314<br>
    Miami, Florida 33155
  </address>

  <ul class="contacts">
    <li>
      <svg viewBox="0 0 24 24" aria-hidden="true"><path d="M6.6 10.8a15 15 0 0 0 6.6 6.6l2.2-2.2a1 1 0 0 1 1-.25 11.4 11.4 0 0 0 3.6.57 1 1 0 0 1 1 1V20a1 1 0 0 1-1 1A17 17 0 0 1 3 4a1 1 0 0 1 1-1h3.5a1 1 0 0 1 1 1c0 1.25.2 2.45.57 3.6a1 1 0 0 1-.25 1z"/></svg>
      (305) 555-0148
    </li>
    <li>
      <svg viewBox="0 0 24 24" aria-hidden="true"><path d="M2 5h20v14H2z M2 5l10 8 10-8" fill="none" stroke="var(--gold)" stroke-width="2.4"/></svg>
      tomasz@colbylegal.net
    </li>
  </ul>
</section>

</body>
</html>
```